Sales Materials Design Project

Introduction

BrivexNET is the world’s leading English language website for expatriates. It was founded in 2000 on the French Riviera and now has 63 local sites around the world in 32 countries and a worldwide site. It has a number of sites under development and it is the intention to continue to grow to 100 live regional sites in 40 countries by December 2012. BrivexNET currently serves over 80 million monthly pageviews to an estimated three million visitors. BrivexNET’s global website can be accessed at www.brivexnet.example

A new website, with a more modern look and feel will be released in early July 2012.

With the new website launch, it is time for us to revisit all our internal and external documentation, bringing it together and up to date with our ambitious growth strategy.
We would like to keep our logo as is.

We will pay £525 for the successful design of the 14 items. We would like to see a range of 3-4 items on Monday 25th June where we would pre-select/approve designs and then agree delivery of all items during the following weeks.

Target Market(s)

Quite a mix – age ranges from 20-70, all types of lifestyle preferences, in locations across the globe – most of our active users visit the website

Industry/Entity Type

Delivery

Requirements
Must have
• We require the design of a series of client facing documents, which should be editable and able to the PDFed without any issues. Preferred formats would be Microsoft Word (locked templates so the design cannot be altered, only text content), and source files should be delivered in Adobe InDesign. All documents should have a common look and feel, and they end up being variations of one.

```html
<!DOCTYPE html>
<html lang="en">
<head>
<meta charset="utf-8">
<title>BrivexNET Training Manual – Stationery Set</title>
<link rel="stylesheet" href="https://fonts.googleapis.com/css2?family=Questrial&family=Arimo&display=swap">
<style>
  :root {
    --backdrop: #2b2724;
    --paper: #ffffff;
    --brand-red: #a51f22;
    --ink: #2a2a2a;
    --rule: #1e1e1e;
    --sky-top: #8d86a8;
    --sky-mid: #b9b3c9;
    --sky-low: #d9c9cf;
    --city: #6b6d78;
    --mist: #c9c6d3;
  }
  * { box-sizing: border-box; margin: 0; padding: 0; }
  html, body { width: 1200px; height: 900px; overflow: hidden; }
  body {
    position: relative;
    background: var(--backdrop);
    font-family: "Questrial", "Helvetica Neue", Arial, sans-serif;
  }

  .sheet {
    position: absolute;
    width: 378px;
    background: var(--paper);
    overflow: hidden;
  }

  /* Cover */
  .sheet--cover { left: 20px; top: 19px; height: 533px; }
  .cover-title {
    position: absolute; right: 16px; top: 25px;
    color: var(--brand-red); font-size: 20px; font-weight: 400;
  }
  .sheet--cover .masthead { top: 228px; }
  .cover-band {
    position: absolute; left: 0; right: 0; top: 281px; bottom: 0;
    background: var(--brand-red);
  }

  /* Masthead shared by all sheets */
  .masthead {
    position: absolute; left: 0; top: 0;
    width: 378px; height: 53px;
  }
  .masthead svg { position: absolute; inset: 0; width: 100%; height: 100%; }
  .brand-name {
    position: absolute; left: 22px; top: 10px;
    font-size: 25px; letter-spacing: -0.5px;
    color: var(--ink); font-weight: 400;
  }

  /* Contents sheet */
  .sheet--contents { left: 404px; top: 118px; height: 532px; }
  .contents-list {
    position: absolute; left: 40px; top: 247px;
    list-style: none;
  }
  .contents-item {
    display: flex; align-items: baseline;
    height: 23px;
  }
  .contents-label {
    width: 115px; font-size: 8px; color: var(--brand-red);
  }
  .contents-number {
    font-size: 19px; color: var(--brand-red); line-height: 1;
  }

  /* Text sheet */
  .sheet--text { left: 789px; top: 325px; height: 535px; }

  .skyline-fade {
    position: absolute; left: 0; right: 0; bottom: 0; height: 60px;
    background:
      linear-gradient(to bottom, rgba(255,255,255,1) 0%, rgba(255,255,255,0) 45%),
      linear-gradient(to bottom, var(--mist) 0%, #bdb7c8 55%, var(--city) 100%);
  }

  .set-title {
    position: absolute; left: 860px; top: 186px;
    font-family: "Arimo", Arial, sans-serif;
    font-size: 31px; color: #ffffff; font-weight: 400;
  }
</style>
</head>
<body>

  <!-- Cover -->
  <section class="sheet sheet--cover">
    <h1 class="cover-title">Training Manual</h1>
    <header class="masthead">
      <svg viewBox="0 0 378 53" role="img" aria-label="City skyline photograph under a lavender evening sky">
        <defs>
          <linearGradient id="sky-cover" x1="0" y1="0" x2="0" y2="1">
            <stop offset="0" stop-color="var(--sky-top)"/>
            <stop offset="0.5" stop-color="var(--sky-mid)"/>
            <stop offset="0.8" stop-color="var(--sky-low)"/>
            <stop offset="1" stop-color="var(--city)"/>
          </linearGradient>
        </defs>
        <path d="M100 53 C150 45 175 5 215 0 L378 0 L378 53 Z" fill="url(#sky-cover)"/>
        <path d="M92 52 C145 46 170 6 215 0" fill="none" stroke="var(--brand-red)" stroke-width="2.5"/>
        <line x1="100" y1="52" x2="378" y2="52" stroke="var(--rule)" stroke-width="2"/>
      </svg>
      <span class="brand-name">BrivexNET</span>
    </header>
    <div class="cover-band"></div>
  </section>

  <!-- Contents -->
  <section class="sheet sheet--contents">
    <header class="masthead">
      <svg viewBox="0 0 378 53" role="img" aria-label="City skyline photograph under a lavender evening sky">
        <defs>
          <linearGradient id="sky-contents" x1="0" y1="0" x2="0" y2="1">
            <stop offset="0" stop-color="var(--sky-top)"/>
            <stop offset="0.5" stop-color="var(--sky-mid)"/>
            <stop offset="0.8" stop-color="var(--sky-low)"/>
            <stop offset="1" stop-color="var(--city)"/>
          </linearGradient>
        </defs>
        <path d="M100 53 C150 45 175 5 215 0 L378 0 L378 53 Z" fill="url(#sky-contents)"/>
        <path d="M92 52 C145 46 170 6 215 0" fill="none" stroke="var(--brand-red)" stroke-width="2.5"/>
        <line x1="100" y1="52" x2="378" y2="52" stroke="var(--rule)" stroke-width="2"/>
      </svg>
      <span class="brand-name">BrivexNET</span>
    </header>
    <ol class="contents-list">
      <li class="contents-item"><span class="contents-label">Index Index Index index</span><span class="contents-number">1</span></li>
      <li class="contents-item"><span class="contents-label">Index Index Index index</span><span class="contents-number">2</span></li>
      <li class="contents-item"><span class="contents-label">Index Index Index index</span><span class="contents-number">3</span></li>
      <li class="contents-item"><span class="contents-label">Index Index Index index</span><span class="contents-number">4</span></li>
      <li class="contents-item"><span class="contents-label">Index Index Index index</span><span class="contents-number">5</span></li>
      <li class="contents-item"><span class="contents-label">Index Index Index index</span><span class="contents-number">6</span></li>
      <li class="contents-item"><span class="contents-label">Index Index Index index</span><span class="contents-number">7</span></li>
      <li class="contents-item"><span class="contents-label">Index Index Index index</span><span class="contents-number">8</span></li>
    </ol>
    <div class="skyline-fade" role="img" aria-label="Faded city skyline photograph along the page foot"></div>
  </section>

  <h2 class="set-title">Training Manual</h2>

  <!-- Text page -->
  <section class="sheet sheet--text">
    <header class="masthead">
      <svg viewBox="0 0 378 53" role="img" aria-label="City skyline photograph under a lavender evening sky">
        <defs>
          <linearGradient id="sky-text" x1="0" y1="0" x2="0" y2="1">
            <stop offset="0" stop-color="var(--sky-top)"/>
            <stop offset="0.5" stop-color="var(--sky-mid)"/>
            <stop offset="0.8" stop-color="var(--sky-low)"/>
            <stop offset="1" stop-color="var(--city)"/>
          </linearGradient>
        </defs>
        <path d="M100 53 C150 45 175 5 215 0 L378 0 L378 53 Z" fill="url(#sky-text)"/>
        <path d="M92 52 C145 46 170 6 215 0" fill="none" stroke="var(--brand-red)" stroke-width="2.5"/>
        <line x1="100" y1="52" x2="378" y2="52" stroke="var(--rule)" stroke-width="2"/>
      </svg>
      <span class="brand-name">BrivexNET</span>
    </header>
    <div class="skyline-fade" role="img" aria-label="Faded city skyline photograph along the page foot"></div>
  </section>

</body>
</html>
```